Kestrel Softball Tournaments Website Design

Our client would like us to design a website. The company is similar to Brightfield Sports USA (https://brightfieldsportsusa.example).

We prefer Adobe Fonts in the design. Lorem ipsum is fine to use for content, except for headers. Please keep track of any images used in your design. We plan on purchasing the images used.

Number of Pages Required

1 page

Font styles to use
Sans Serif

Colors
0054AA
0677BA
7BADD7
CADEEF
E8F1F8

```html
<!DOCTYPE html>
<html lang="en">
<head>
<meta charset="utf-8">
<title>Kestrel Softball Tournaments</title>
<link rel="stylesheet" href="https://fonts.googleapis.com/css2?family=Montserrat:wght@500;600;700&display=swap">
<style>
:root{
  --blue-strong:#0054AA;
  --blue-bright:#0677BA;
  --blue-soft:#7BADD7;
  --blue-pale:#CADEEF;
  --blue-mist:#E8F1F8;
  --blue-deep:#00397a;
  --blue-ink:#06264d;
  --white:#ffffff;
  --field-green:#8fae5a;
  --sky-blue:#3f45a8;
}
*{margin:0;padding:0;box-sizing:border-box}
html,body{width:1200px;height:2699px;overflow:hidden}
body{font-family:"Montserrat",sans-serif;color:var(--white);position:relative;background:var(--blue-ink)}
section{position:absolute;left:0;width:1200px}
.gradient-band{background:linear-gradient(90deg,var(--blue-bright) 0%,var(--blue-strong) 55%,var(--blue-deep) 100%)}
.ink-band{background:var(--blue-ink)}
.hero{top:0;height:675px}
.feature{top:675px;height:675px}
.testimonials{top:1350px;height:675px}
.footer{top:2025px;height:674px}
.brand-mark{position:absolute;display:flex;align-items:center;gap:12px;font-weight:700;color:var(--white);line-height:1.05}
.brand-mark .dot{width:26px;height:26px;border-radius:50%;background:var(--blue-pale);flex:none}
.hero .brand-mark{left:84px;top:145px;font-size:30px}
.hero-title{position:absolute;left:80px;top:326px;font-size:60px;font-weight:700;line-height:61px;letter-spacing:.3px}
.btn{position:absolute;display:flex;align-items:center;justify-content:center;border-radius:26px;font-weight:700;font-size:22px;text-decoration:none}
.btn-light{left:80px;top:574px;width:210px;height:50px;background:var(--blue-mist);color:var(--blue-strong)}
.btn-accent{left:80px;top:574px;width:210px;height:50px;background:var(--blue-bright);color:var(--white)}
.photo{position:absolute;width:482px;height:482px;border-radius:50%;left:650px;top:68px}
.photo-player{background:radial-gradient(circle at 50% 55%,#d9d9df 0%,#b8bcc2 25%,var(--field-green) 60%,#6d8a45 100%)}
.photo-gear{top:67px;background:linear-gradient(160deg,var(--sky-blue) 0%,#2b2f7a 40%,#8a5a35 60%,#c99a20 85%,#1a1a1a 100%)}
.feature-title{position:absolute;left:80px;top:193px;font-size:62px;font-weight:700;line-height:74px}
.feature-text{position:absolute;left:80px;top:407px;width:470px;font-size:22px;font-weight:600;line-height:33px;color:var(--blue-mist)}
.section-title{position:absolute;left:0;width:1200px;top:104px;text-align:center;font-size:64px;font-weight:700}
.quote{position:absolute;width:500px;font-size:17px;font-weight:600;line-height:24.6px}
.quote .cite{display:block}
.q1{left:67px;top:279px}.q2{left:656px;top:279px}
.q3{left:67px;top:431px}.q4{left:656px;top:431px}
.info-col{position:absolute;top:67px;width:380px;text-align:center;font-size:21px;font-weight:500;line-height:31px;color:var(--blue-mist)}
.info-col h3{font-size:23px;font-weight:700;margin-bottom:33px;color:var(--white)}
.info-left{left:214px}.info-right{left:605px}
.footer .brand-mark{left:0;width:1200px;justify-content:center;top:467px;font-size:28px}
.follow{position:absolute;left:470px;top:598px;display:flex;align-items:center;gap:30px}
.follow span{font-size:17px;font-weight:700;letter-spacing:.5px}
.social{display:flex;gap:18px}
.social i{display:block;width:26px;height:26px;border-radius:50%;background:var(--blue-soft)}
</style>
</head>
<body>

<section class="hero gradient-band">
  <div class="brand-mark"><span class="dot"></span><span>Kestrel<br>Softball</span></div>
  <h1 class="hero-title">Incredible<br>Individual<br>Performances</h1>
  <a class="btn btn-light" href="#">Learn More</a>
  <div class="photo photo-player" role="img" aria-label="Photo of a softball catcher crouching and catching a ball in front of a chain-link fence"></div>
</section>

<section class="feature ink-band">
  <h2 class="feature-title">Kestrel<br>Softball</h2>
  <p class="feature-text">Use this space to highlight your most popular services. You can also use this for your flagship products.</p>
  <a class="btn btn-accent" href="#">Sign up here</a>
  <div class="photo photo-gear" role="img" aria-label="Photo of softball gear: a bat, a glove with a yellow ball and a yellow batting helmet"></div>
</section>

<section class="testimonials gradient-band">
  <h2 class="section-title">What They're Saying</h2>
  <blockquote class="quote q1">"Boost your product and service's credibility by adding testimonials from your clients. People love recommendations so feedback from others who've tried it is invaluable."<span class="cite">— Lorna Vickers</span></blockquote>
  <blockquote class="quote q2">"Boost your product and service's credibility by adding testimonials from your clients. People love recommendations include feedback from others."<span class="cite">— Talia Brennan</span></blockquote>
  <blockquote class="quote q3">"Boost your product and service's credibility by adding testimonials from your clients. People love recommendations so feedback from others who've tried it is invaluable.<br><br>Just add them here!"<span class="cite">— Amos Kirui</span></blockquote>
  <blockquote class="quote q4">"Boost your product and service's credibility by adding testimonials from your clients. People love recommendations so feedback from others who've tried it is invaluable."<span class="cite">— Owen Lachance</span></blockquote>
</section>

<section class="footer ink-band">
  <div class="info-col info-left">
    <h3>Contact Us</h3>
    <p>Monday to Friday<br>9:00 am to 6:00 pm<br>Saturday<br>9:00 am to 12 noon</p>
    <p style="margin-top:31px">Sunday by appointment only.</p>
  </div>
  <div class="info-col info-right">
    <h3>Business Hours</h3>
    <p>48 Larkspur Ave.<br>Millbrook, ST 20418</p>
    <p style="margin-top:31px">hello@kestrelsoftball.example</p>
  </div>
  <div class="brand-mark"><span class="dot"></span><span>Kestrel Softball</span></div>
  <div class="follow">
    <span>FOLLOW US</span>
    <div class="social" aria-label="Social links"><i></i><i></i><i></i></div>
  </div>
</section>

</body>
</html>
```